Mimi Harlan Poster

Need a design for poster for my daughter. Performer for school aged kids. Would like her name "MIMI or Mimi" on the poster- can change background

Target Market(s)

school aged kids

Industry/Entity Type

School

Requirements
Must have
• name - MIMI or Mimi on poster

```html
<!DOCTYPE html>
<html lang="en">
<head>
<meta charset="UTF-8">
<title>Mimi Harlan Poster</title>
<link href="https://fonts.googleapis.com/css2?family=Alfa+Slab+One&display=swap" rel="stylesheet">
<style>
  :root {
    --page: #ffffff;
    --navy: #2e3f8f;
    --navy-dark: #1f2c6b;
    --sun-top: #fff200;
    --sun-bottom: #ffc400;
    --cream: #f6efe2;
    --ribbon: #e31e24;
    --ribbon-edge: #3b3f8c;
    --tile: #1e9be6;
    --tile-shadow: #0d4f86;
    --letter: #d8161c;
    --photo-warm: #8a5a3c;
    --photo-soft: #c9b08a;
    --streamer-magenta: rgba(190, 40, 140, 0.45);
    --streamer-teal: rgba(20, 150, 140, 0.40);
    --streamer-red: rgba(220, 40, 50, 0.42);
    --streamer-blue: rgba(40, 120, 210, 0.40);
    --streamer-violet: rgba(120, 50, 170, 0.38);
  }
  * { margin: 0; padding: 0; box-sizing: border-box; }
  html, body {
    width: 900px;
    height: 1200px;
    overflow: hidden;
    background: var(--page);
  }
  .canvas {
    position: relative;
    width: 900px;
    height: 1200px;
  }
  .poster {
    position: absolute;
    left: 112px;
    top: 55px;
    width: 678px;
    height: 1086px;
    overflow: hidden;
  }
  .poster__backdrop {
    position: absolute;
    inset: 0;
    background: linear-gradient(180deg, var(--sun-top) 0%, var(--sun-bottom) 100%);
  }
  .poster__streamers {
    position: absolute;
    inset: 0;
    background:
      radial-gradient(ellipse 130px 60px at 120px 90px, var(--streamer-magenta), transparent 70%),
      radial-gradient(ellipse 140px 70px at 380px 80px, var(--streamer-teal), transparent 70%),
      radial-gradient(ellipse 150px 80px at 580px 120px, var(--streamer-red), transparent 70%),
      radial-gradient(ellipse 140px 60px at 260px 190px, var(--streamer-red), transparent 70%),
      radial-gradient(ellipse 140px 70px at 520px 230px, var(--streamer-teal), transparent 70%),
      radial-gradient(ellipse 60px 140px at 40px 310px, var(--streamer-blue), transparent 70%),
      radial-gradient(ellipse 70px 160px at 640px 420px, var(--streamer-red), transparent 70%),
      radial-gradient(ellipse 50px 120px at 20px 600px, var(--streamer-teal), transparent 70%),
      radial-gradient(ellipse 150px 70px at 110px 820px, var(--streamer-red), transparent 70%),
      radial-gradient(ellipse 160px 80px at 300px 840px, var(--streamer-magenta), transparent 70%),
      radial-gradient(ellipse 150px 70px at 560px 860px, var(--streamer-teal), transparent 70%),
      radial-gradient(ellipse 170px 70px at 160px 980px, var(--streamer-blue), transparent 70%),
      radial-gradient(ellipse 150px 80px at 420px 960px, var(--streamer-violet), transparent 70%),
      radial-gradient(ellipse 140px 60px at 600px 1020px, var(--streamer-red), transparent 70%),
      radial-gradient(ellipse 160px 60px at 300px 1050px, var(--streamer-magenta), transparent 70%);
  }
  .poster__band {
    position: absolute;
    left: 0;
    width: 100%;
    height: 16px;
    background: var(--navy);
  }
  .poster__band--top { top: 0; }
  .poster__band--bottom { bottom: 0; }
  .emblem {
    position: absolute;
    left: 0;
    top: 0;
    width: 678px;
    height: 1086px;
  }
  .name-tiles {
    position: absolute;
    left: 193px;
    top: 624px;
    display: flex;
    gap: 3px;
  }
  .name-tiles__tile {
    width: 71px;
    height: 74px;
    background: var(--tile);
    box-shadow: 3px 4px 0 var(--tile-shadow);
    display: flex;
    align-items: center;
    justify-content: center;
    font-family: "Alfa Slab One", serif;
    font-size: 50px;
    line-height: 1;
    color: var(--letter);
    text-shadow: 2px 2px 0 var(--navy-dark);
  }
</style>
</head>
<body>
<div class="canvas">
  <main class="poster">
    <div class="poster__backdrop"></div>
    <div class="poster__streamers" role="img" aria-label="Colourful curling party streamers and confetti stars scattered across the yellow background"></div>
    <div class="poster__band poster__band--top"></div>
    <div class="poster__band poster__band--bottom"></div>

    <svg class="emblem" viewBox="0 0 678 1086" xmlns="http://www.w3.org/2000/svg">
      <defs>
        <radialGradient id="portrait-tone" cx="50%" cy="40%" r="60%">
          <stop offset="0%" stop-color="var(--photo-soft)"/>
          <stop offset="100%" stop-color="var(--photo-warm)"/>
        </radialGradient>
      </defs>

      <!-- starburst seal -->
      <circle cx="339" cy="449" r="262" fill="none" stroke="var(--navy)" stroke-width="26" stroke-dasharray="4 5"/>
      <circle cx="339" cy="449" r="256" fill="var(--navy)"/>
      <circle cx="339" cy="449" r="242" fill="none" stroke="#ffffff" stroke-width="9" stroke-dasharray="0 16" stroke-linecap="round"/>
      <circle cx="339" cy="449" r="226" fill="var(--cream)"/>
      <circle cx="339" cy="449" r="206" fill="var(--navy)"/>
      <circle cx="339" cy="449" r="190" fill="none" stroke="var(--ribbon)" stroke-width="8" stroke-dasharray="0 15" stroke-linecap="round"/>

      <!-- portrait window -->
      <circle cx="339" cy="440" r="172" fill="url(#portrait-tone)" role="img" aria-label="Portrait photo of Mimi Harlan smiling, in a yellow top and white cardigan"/>

      <!-- ribbon tails, tucked behind the centre panel -->
      <polygon points="0,646 158,646 166,730 0,736 46,691" fill="var(--ribbon)" stroke="var(--ribbon-edge)" stroke-width="3" stroke-linejoin="round"/>
      <polygon points="678,646 520,646 512,730 678,736 632,691" fill="var(--ribbon)" stroke="var(--ribbon-edge)" stroke-width="3" stroke-linejoin="round"/>
      <!-- ribbon centre -->
      <path d="M143 604 Q339 586 535 604 L552 742 Q339 716 126 742 Z" fill="var(--ribbon)" stroke="var(--ribbon-edge)" stroke-width="3" stroke-linejoin="round"/>
    </svg>

    <div class="name-tiles" aria-label="MIMI">
      <span class="name-tiles__tile">M</span>
      <span class="name-tiles__tile">I</span>
      <span class="name-tiles__tile">M</span>
      <span class="name-tiles__tile">I</span>
    </div>
  </main>
</div>
</body>
</html>
```